Korvix App Graphics Design

Our application promotes location based self expression via pictures and text. The primary focus of the application is on the content posted and not on the person that posted it.

We want a very clean and fresh design that evokes positive energy. Our site is unique so our design should be as well. People will reveal thoughts on our site, so the design should convey a "revealing" feel. Our site is a place where people are comfortable to freely express themselves. Colors we have in mind are blue and green hues with earth tones for background.

Our project is to design ten screens for our Korvix application at resolution of 1136-by-640 pixels:

Feed Screen
Camera Screen
Post Screen
Check In Screen
Approval Screen
Map Screen
Flag Screen
Feed Select Screen
Export Screen
Menu Screen

In the contest phase we will require only three screens to be submitted. The screens we require to be submitted are: Feed Screen; Map Screen and Camera Screen. The designer we select as the winner of the competition will then complete the project and deliver a total of the ten screens described above in the handover phase.

We have attached a document below with detailed specs of each screen, we ask for your innovation to bring these screens to life through your design.
Updates

We want to clarify one aspect regarding the VISOR: the visor needs to be transparent so that when the picture scrolls underneath it, you can still see the picture underneath the visor.

Hi Everyone,

We have noticed that some designers need clarification regarding the visor element in the feed screen.
I have attached two examples to our brief area called:
Visor Example 1 and Visor Example 2

Please note that these are not the style we are looking for but are a good example to the concept of a Transparent Visor above the feed stream. We are looking for you guys to come up with a Visor concept that is consistent with the style of the design you are submitting.

Thanks,

Bo

Target Market(s)

People 17-40 who want to share their thought about the world around them.

Industry/Entity Type

Flag

Font styles to use
Sans Serif
Other font styles liked:
• We like “Helvetica New” or “Avenir” but are flexible

Requirements
Must have
• Visor component should look innovative.

```html
<!DOCTYPE html>
<html lang="en">
<head>
<meta charset="utf-8">
<title>Korvix – Feed Screen</title>
<link href="https://fonts.googleapis.com/css2?family=Arimo:wght@400;700&family=Open+Sans:wght@400;600&family=Roboto+Condensed:wght@400;700&display=swap" rel="stylesheet">
<style>
  :root {
    --canvas: #ffffff;
    --status-black: #000000;
    --leaf-green: #7ba700;
    --leaf-green-dark: #3f5a00;
    --wood-light: #f3d9a8;
    --wood-mid: #e6c088;
    --wood-edge: #c9985a;
    --sky-blue: #55b5de;
    --deep-blue: #1f6f99;
    --mist-grey: #ececec;
    --band-grey: #d9d9d9;
    --ink: #111111;
    --ink-soft: #2b2b2b;
    --white: #ffffff;
  }
  * { box-sizing: border-box; margin: 0; padding: 0; }
  html, body { width: 1000px; height: 1200px; overflow: hidden; background: var(--canvas); }
  .canvas { position: relative; width: 1000px; height: 1200px; overflow: hidden; }

  .screen { position: absolute; width: 640px; height: 1136px; overflow: hidden; background: var(--mist-grey); }
  .screen.full { left: 30px; top: 32px; }
  .screen.preview { left: 704px; top: 290px; transform: scale(0.4); transform-origin: 0 0; }

  .status-bar { position: absolute; left: 0; top: 0; width: 640px; height: 40px; background: var(--status-black); color: var(--white);
    font-family: "Arimo", Arial, sans-serif; font-weight: 700; font-size: 25px; }
  .status-bar .carrier { position: absolute; left: 8px; top: 6px; display: flex; align-items: flex-end; gap: 6px; }
  .status-bar .clock { position: absolute; left: 0; right: 0; top: 6px; text-align: center; }
  .status-bar .indicators { position: absolute; right: 8px; top: 7px; }

  .nav-bar { position: absolute; left: 0; top: 40px; width: 640px; height: 88px; background: var(--leaf-green); }
  .nav-bar .title { position: absolute; left: 0; right: 0; top: 20px; text-align: center; color: var(--white);
    font-family: "Roboto Condensed", "Arial Narrow", sans-serif; font-weight: 700; font-size: 40px; }
  .nav-button { position: absolute; top: 23px; width: 44px; height: 44px; }
  .nav-button.menu { left: 14px; }
  .nav-button.search { right: 14px; }

  .visor { position: absolute; left: 0; top: 128px; width: 640px; height: 95px;
    background: linear-gradient(180deg, rgba(243,217,168,.75), rgba(230,192,136,.7)); }
  .visor .plaque { position: absolute; left: 10px; top: 10px; width: 620px; height: 78px; border-radius: 6px;
    background: linear-gradient(180deg, var(--wood-light), var(--wood-mid)); border: 2px solid var(--wood-edge);
    box-shadow: inset 0 1px 0 rgba(255,255,255,.6), 0 2px 3px rgba(0,0,0,.2);
    display: flex; align-items: center; justify-content: center; padding-right: 16px;
    font-family: "Arimo", Arial, sans-serif; font-weight: 700; font-size: 44px; color: var(--ink); }

  .post-photo { position: absolute; left: 0; top: 223px; width: 640px; height: 583px;
    background: radial-gradient(ellipse at 50% 45%, #e9cdb8 0%, #cdb79e 30%, #b9c98a 62%, #a88d6c 100%); }
  .photo-action { position: absolute; top: 28px; width: 62px; height: 62px; }
  .photo-action.flag { left: 28px; }
  .photo-action.share { right: 27px; }

  .post-meta { position: absolute; left: 0; top: 768px; width: 640px; height: 38px; background: rgba(60,60,60,.55);
    color: var(--white); font-family: "Open Sans", Arial, sans-serif; font-size: 20px; line-height: 38px; }
  .post-meta .distance { position: absolute; left: 20px; }
  .post-meta .score { position: absolute; left: 314px; }
  .post-meta .age { position: absolute; right: 20px; }

  .vote-row { position: absolute; left: 0; top: 806px; width: 640px; height: 92px; background: var(--mist-grey); }
  .vote-button { position: absolute; top: 11px; width: 305px; height: 70px; background: var(--sky-blue); border-radius: 4px;
    box-shadow: 0 3px 0 var(--deep-blue); overflow: hidden;
    font-family: "Roboto Condensed", "Arial Narrow", sans-serif; font-size: 34px; color: var(--white); }
  .vote-button.promote { left: 10px; }
  .vote-button.demote { left: 325px; }
  .vote-button .tab { position: absolute; left: 0; top: 0; }
  .vote-button .label { position: absolute; left: 95px; top: 13px; }

  .venue { position: absolute; left: 0; top: 898px; width: 640px; height: 57px; background: var(--band-grey);
    padding: 6px 10px; font-style: normal;
    font-family: "Roboto Condensed", "Arial Narrow", sans-serif; font-size: 17px; line-height: 23px; color: var(--ink-soft); }

  .next-photo { position: absolute; left: 0; top: 955px; width: 640px; height: 80px;
    background: linear-gradient(180deg, #cfc6b4 0%, #b9ad95 45%, #9a7a52 70%, #d8d2c4 100%); }

  .tab-bar { position: absolute; left: 0; top: 1033px; width: 640px; height: 103px; background: var(--leaf-green);
    border-top: 3px solid var(--leaf-green-dark); color: var(--white);
    font-family: "Roboto Condensed", "Arial Narrow", sans-serif; font-weight: 700; font-size: 22px; }
  .tab-item { position: absolute; top: 12px; text-align: center; }
  .tab-item.camera { left: 28px; }
  .tab-item.badge { right: 34px; }
  .tab-item svg { display: block; margin: 0 auto 4px; }
</style>
</head>
<body>
<div class="canvas">

  <main class="screen full">
    <header class="status-bar">
      <div class="carrier">
        <svg width="40" height="20" viewBox="0 0 40 20" aria-hidden="true">
          <rect x="0" y="14" width="5" height="6" fill="#fff"/><rect x="8" y="11" width="5" height="9" fill="#fff"/>
          <rect x="16" y="8" width="5" height="12" fill="#fff"/><rect x="24" y="5" width="5" height="15" fill="#fff"/>
          <rect x="32" y="2" width="5" height="18" fill="#fff"/>
        </svg>
        <span>Bet</span>
      </div>
      <div class="clock">4:20 PM</div>
      <svg class="indicators" width="145" height="26" viewBox="0 0 145 26" aria-hidden="true">
        <circle cx="10" cy="13" r="10" fill="#fff"/><path d="M10 6v7h5" stroke="#000" stroke-width="2.5" fill="none"/>
        <path d="M34 14l20-9-9 20-2-9z" fill="#fff"/>
        <circle cx="72" cy="13" r="11" stroke="#fff" stroke-width="2.5" fill="none"/>
        <rect x="66" y="11" width="12" height="9" fill="#fff"/><path d="M68 11v-3a4 4 0 0 1 8 0v3" stroke="#fff" stroke-width="2" fill="none"/>
        <rect x="96" y="3" width="40" height="20" rx="3" stroke="#fff" stroke-width="2.5" fill="none"/>
        <rect x="100" y="7" width="32" height="12" fill="#fff"/><rect x="138" y="9" width="4" height="8" fill="#fff"/>
      </svg>
    </header>

    <nav class="nav-bar">
      <svg class="nav-button menu" viewBox="0 0 44 44" aria-label="Menu" role="img">
        <circle cx="22" cy="22" r="21" fill="#e6e6e6" stroke="#aaa"/>
        <rect x="12" y="13" width="20" height="4" rx="2" fill="#444"/><rect x="12" y="20" width="20" height="4" rx="2" fill="#444"/>
        <rect x="12" y="27" width="20" height="4" rx="2" fill="#444"/>
      </svg>
      <div class="title">Feed Name</div>
      <svg class="nav-button search" viewBox="0 0 44 44" aria-label="Search" role="img">
        <circle cx="22" cy="22" r="21" fill="#e6e6e6" stroke="#aaa"/>
        <circle cx="19" cy="19" r="7" stroke="#444" stroke-width="3.5" fill="none"/>
        <path d="M24 24l7 7" stroke="#444" stroke-width="4.5" stroke-linecap="round"/>
      </svg>
    </nav>

    <section class="post-photo" role="img" aria-label="Posted photo: a child wrapped in a knitted scarf holding a blue mug on a bed">
      <svg class="photo-action flag" viewBox="0 0 62 62" aria-label="Flag post" role="img">
        <circle cx="31" cy="31" r="29" fill="var(--deep-blue)" stroke="#fff" stroke-width="3"/>
        <path d="M22 17v30" stroke="#fff" stroke-width="3" stroke-linecap="round"/>
        <path d="M23 18c6-3 10 3 18 0v13c-8 3-12-3-18 0z" fill="#fff"/>
      </svg>
      <svg class="photo-action share" viewBox="0 0 62 62" aria-label="Share post" role="img">
        <circle cx="31" cy="31" r="29" fill="var(--deep-blue)" stroke="#fff" stroke-width="3"/>
        <path d="M18 44c0-12 7-18 17-18v-7l12 11-12 11v-7c-8 0-13 3-17 10z" fill="#fff"/>
      </svg>
    </section>

    <div class="visor"><div class="plaque">Lorem ipsum</div></div>

    <div class="post-meta">
      <span class="distance">0.01 mi</span>
      <span class="score">0</span>
      <span class="age">few hours ago</span>
    </div>

    <section class="vote-row">
      <div class="vote-button promote">
        <svg class="tab" width="92" height="70" viewBox="0 0 92 70" aria-hidden="true">
          <path d="M0 0h72l20 35-20 35H0z" fill="var(--deep-blue)"/>
          <circle cx="32" cy="35" r="15" stroke="#fff" stroke-width="2.5" fill="none"/>
          <circle cx="26" cy="31" r="2" fill="#fff"/><circle cx="38" cy="31" r="2" fill="#fff"/>
          <path d="M24 39q8 8 16 0" stroke="#fff" stroke-width="2.5" fill="none"/>
        </svg>
        <span class="label">Promote</span>
      </div>
      <div class="vote-button demote">
        <svg class="tab" width="92" height="70" viewBox="0 0 92 70" aria-hidden="true">
          <path d="M0 0h72l20 35-20 35H0z" fill="var(--deep-blue)"/>
          <circle cx="32" cy="35" r="15" stroke="#fff" stroke-width="2.5" fill="none"/>
          <circle cx="26" cy="31" r="2" fill="#fff"/><circle cx="38" cy="31" r="2" fill="#fff"/>
          <path d="M24 43q8-8 16 0" stroke="#fff" stroke-width="2.5" fill="none"/>
        </svg>
        <span class="label">Demote</span>
      </div>
    </section>

    <address class="venue">Maple Grill,<br>48 Harbor Lane, Fairview, NY 10422</address>

    <div class="next-photo" role="img" aria-label="Next posted photo: a window with draped patterned curtains"></div>

    <footer class="tab-bar">
      <div class="tab-item camera">
        <svg width="54" height="44" viewBox="0 0 54 44" aria-hidden="true">
          <rect x="2" y="8" width="50" height="34" rx="4" fill="#111"/><rect x="8" y="3" width="12" height="7" fill="#111"/>
          <circle cx="31" cy="25" r="11" fill="var(--leaf-green)"/><circle cx="31" cy="25" r="7" fill="#111"/>
          <rect x="7" y="13" width="6" height="4" fill="var(--leaf-green)"/>
        </svg>
        Camera
      </div>
      <div class="tab-item badge">
        <svg width="44" height="44" viewBox="0 0 44 44" aria-hidden="true">
          <path d="M12 28l-6 14 8-3 4 5 5-13z M32 28l6 14-8-3-4 5-5-13z" fill="#111"/>
          <path d="M22 2l4 4 5-1 1 5 5 2-2 5 2 5-5 2-1 5-5-1-4 4-4-4-5 1-1-5-5-2 2-5-2-5 5-2 1-5 5 1z" fill="#111"/>
          <circle cx="22" cy="18" r="6" fill="var(--leaf-green)"/>
        </svg>
        Badge
      </div>
    </footer>
  </main>

  <aside class="screen preview" aria-label="Feed screen preview">
    <header class="status-bar">
      <div class="carrier">
        <svg width="40" height="20" viewBox="0 0 40 20" aria-hidden="true">
          <rect x="0" y="14" width="5" height="6" fill="#fff"/><rect x="8" y="11" width="5" height="9" fill="#fff"/>
          <rect x="16" y="8" width="5" height="12" fill="#fff"/><rect x="24" y="5" width="5" height="15" fill="#fff"/>
          <rect x="32" y="2" width="5" height="18" fill="#fff"/>
        </svg>
        <span>Bet</span>
      </div>
      <div class="clock">4:20 PM</div>
      <svg class="indicators" width="145" height="26" viewBox="0 0 145 26" aria-hidden="true">
        <circle cx="10" cy="13" r="10" fill="#fff"/><path d="M10 6v7h5" stroke="#000" stroke-width="2.5" fill="none"/>
        <path d="M34 14l20-9-9 20-2-9z" fill="#fff"/>
        <circle cx="72" cy="13" r="11" stroke="#fff" stroke-width="2.5" fill="none"/>
        <rect x="66" y="11" width="12" height="9" fill="#fff"/><path d="M68 11v-3a4 4 0 0 1 8 0v3" stroke="#fff" stroke-width="2" fill="none"/>
        <rect x="96" y="3" width="40" height="20" rx="3" stroke="#fff" stroke-width="2.5" fill="none"/>
        <rect x="100" y="7" width="32" height="12" fill="#fff"/><rect x="138" y="9" width="4" height="8" fill="#fff"/>
      </svg>
    </header>

    <nav class="nav-bar">
      <svg class="nav-button menu" viewBox="0 0 44 44" aria-hidden="true">
        <circle cx="22" cy="22" r="21" fill="#e6e6e6" stroke="#aaa"/>
        <rect x="12" y="13" width="20" height="4" rx="2" fill="#444"/><rect x="12" y="20" width="20" height="4" rx="2" fill="#444"/>
        <rect x="12" y="27" width="20" height="4" rx="2" fill="#444"/>
      </svg>
      <div class="title">Feed Name</div>
      <svg class="nav-button search" viewBox="0 0 44 44" aria-hidden="true">
        <circle cx="22" cy="22" r="21" fill="#e6e6e6" stroke="#aaa"/>
        <circle cx="19" cy="19" r="7" stroke="#444" stroke-width="3.5" fill="none"/>
        <path d="M24 24l7 7" stroke="#444" stroke-width="4.5" stroke-linecap="round"/>
      </svg>
    </nav>

    <section class="post-photo" role="img" aria-label="Posted photo: a child wrapped in a knitted scarf holding a blue mug on a bed">
      <svg class="photo-action flag" viewBox="0 0 62 62" aria-hidden="true">
        <circle cx="31" cy="31" r="29" fill="var(--deep-blue)" stroke="#fff" stroke-width="3"/>
        <path d="M22 17v30" stroke="#fff" stroke-width="3" stroke-linecap="round"/>
        <path d="M23 18c6-3 10 3 18 0v13c-8 3-12-3-18 0z" fill="#fff"/>
      </svg>
      <svg class="photo-action share" viewBox="0 0 62 62" aria-hidden="true">
        <circle cx="31" cy="31" r="29" fill="var(--deep-blue)" stroke="#fff" stroke-width="3"/>
        <path d="M18 44c0-12 7-18 17-18v-7l12 11-12 11v-7c-8 0-13 3-17 10z" fill="#fff"/>
      </svg>
    </section>

    <div class="visor"><div class="plaque">Lorem ipsum</div></div>

    <div class="post-meta">
      <span class="distance">0.01 mi</span>
      <span class="score">0</span>
      <span class="age">few hours ago</span>
    </div>

    <section class="vote-row">
      <div class="vote-button promote">
        <svg class="tab" width="92" height="70" viewBox="0 0 92 70" aria-hidden="true">
          <path d="M0 0h72l20 35-20 35H0z" fill="var(--deep-blue)"/>
          <circle cx="32" cy="35" r="15" stroke="#fff" stroke-width="2.5" fill="none"/>
          <circle cx="26" cy="31" r="2" fill="#fff"/><circle cx="38" cy="31" r="2" fill="#fff"/>
          <path d="M24 39q8 8 16 0" stroke="#fff" stroke-width="2.5" fill="none"/>
        </svg>
        <span class="label">Promote</span>
      </div>
      <div class="vote-button demote">
        <svg class="tab" width="92" height="70" viewBox="0 0 92 70" aria-hidden="true">
          <path d="M0 0h72l20 35-20 35H0z" fill="var(--deep-blue)"/>
          <circle cx="32" cy="35" r="15" stroke="#fff" stroke-width="2.5" fill="none"/>
          <circle cx="26" cy="31" r="2" fill="#fff"/><circle cx="38" cy="31" r="2" fill="#fff"/>
          <path d="M24 43q8-8 16 0" stroke="#fff" stroke-width="2.5" fill="none"/>
        </svg>
        <span class="label">Demote</span>
      </div>
    </section>

    <address class="venue">Maple Grill,<br>48 Harbor Lane, Fairview, NY 10422</address>

    <div class="next-photo" role="img" aria-label="Next posted photo: a window with draped patterned curtains"></div>

    <footer class="tab-bar">
      <div class="tab-item camera">
        <svg width="54" height="44" viewBox="0 0 54 44" aria-hidden="true">
          <rect x="2" y="8" width="50" height="34" rx="4" fill="#111"/><rect x="8" y="3" width="12" height="7" fill="#111"/>
          <circle cx="31" cy="25" r="11" fill="var(--leaf-green)"/><circle cx="31" cy="25" r="7" fill="#111"/>
          <rect x="7" y="13" width="6" height="4" fill="var(--leaf-green)"/>
        </svg>
        Camera
      </div>
      <div class="tab-item badge">
        <svg width="44" height="44" viewBox="0 0 44 44" aria-hidden="true">
          <path d="M12 28l-6 14 8-3 4 5 5-13z M32 28l6 14-8-3-4 5-5-13z" fill="#111"/>
          <path d="M22 2l4 4 5-1 1 5 5 2-2 5 2 5-5 2-1 5-5-1-4 4-4-4-5 1-1-5-5-2 2-5-2-5 5-2 1-5 5 1z" fill="#111"/>
          <circle cx="22" cy="18" r="6" fill="var(--leaf-green)"/>
        </svg>
        Badge
      </div>
    </footer>
  </aside>

</div>
</body>
</html>
```